Pause Your Day And Browse- PYDB poster

I am the Vice President of Advocacy for the Coastline Shelfkeepers Guild. I am looking to have a set of posters made for PYDB (Pause Your Day and Browse) October 23. PYDB is a time when all school children in BC are encouraged to Pause Your Day and Browse for 15-20 minutes at some point in their day.

I would like to get a set of 2 digital posters designed (if possible it would be nice to have the option to print to both 11 x 17 and 8.5 x 11 paper). We need a poster that is high school (Grade 8-12) appropriate and one that is elementary (Grade k-7) appropriate. Both posters need to be replicated in French. All posters need to have the KWNU logo on them as well as the Coastline Shelfkeepers Guild Logo.

Here is a link to last year's successful design http://kwnu-example.org/csg/info/advocacy.html
There are two additional samples in the uploaded files section.

Each poster needs to have the following information:

-Pause Your Day and Browse (PYDB)
- The date Monday, October 23, 2017
-the logo for the KWNU (attached)
-the logo for the CSG (attached)- the logos do not have to be large.

Target Market(s)

Children ages 5-12 and 12-17 as well as their teachers

Industry/Entity Type

Teacher

Font styles to use
Sans Serif

Requirements
Must have
• Must have both logos- colours may be changed for either or both
Nice to have
• Clear, Bright lettering. Images of child or children enjoying reading
Should not have
• stereotypes

```html
<!DOCTYPE html>
<html lang="en">
<head>
<meta charset="utf-8">
<title>Pause Your Day And Browse – PYDB</title>
<link rel="stylesheet" href="https://fonts.googleapis.com/css2?family=Josefin+Sans:wght@300;400;600&display=swap">
<style>
  :root {
    --paper-light: #f5f5f0;
    --paper-edge: #dcdcd2;
    --headline: #ff3a12;
    --ribbon: #ff3a12;
    --ribbon-text: #ffffff;
    --union-blue: #0c2a9e;
    --guild-ink: #2b1a0a;
    --book-brown: #7b4a50;
    --book-teal: #4fe0bb;
    --book-red: #ff3a1c;
    --book-orange: #f7a21b;
    --book-page: #f3f3ef;
  }
  html, body {
    margin: 0;
    padding: 0;
    overflow: hidden;
  }
  .poster {
    position: relative;
    width: 1200px;
    height: 777px;
    overflow: hidden;
    background: radial-gradient(ellipse at 50% 48%, var(--paper-light) 0%, #ecece5 55%, var(--paper-edge) 100%);
    font-family: "Josefin Sans", sans-serif;
  }
  .book-frame {
    position: absolute;
    inset: 0;
    width: 1200px;
    height: 777px;
  }
  .guild-mark {
    position: absolute;
    left: 26px;
    top: 42px;
    margin: 0;
    font-size: 30px;
    font-weight: 600;
    color: var(--guild-ink);
    letter-spacing: 1px;
    transform: rotate(-8deg);
  }
  .union-mark {
    position: absolute;
    left: 0;
    right: 0;
    top: 196px;
    display: flex;
    justify-content: center;
    align-items: center;
    gap: 12px;
  }
  .union-mark__dot {
    width: 34px;
    height: 34px;
    border-radius: 50%;
    background: var(--union-blue);
  }
  .union-mark__name {
    font-size: 40px;
    font-weight: 600;
    color: var(--union-blue);
    letter-spacing: 2px;
    line-height: 1;
    padding-top: 6px;
  }
  .event-title {
    position: absolute;
    left: 0;
    right: 0;
    top: 290px;
    margin: 0;
    text-align: center;
    font-size: 176px;
    font-weight: 300;
    line-height: 1;
    letter-spacing: 4px;
    color: var(--headline);
  }
  .event-tagline {
    position: absolute;
    left: 0;
    right: 0;
    top: 458px;
    margin: 0;
    display: flex;
    justify-content: center;
    align-items: center;
    gap: 12px;
    font-size: 29px;
    font-weight: 300;
    color: var(--headline);
    text-transform: uppercase;
    line-height: 1;
  }
  .event-tagline__text { padding-top: 5px; }
  .event-tagline svg { width: 24px; height: 24px; fill: var(--headline); }
  .event-date {
    position: absolute;
    left: 398px;
    top: 512px;
    width: 392px;
    height: 56px;
  }
  .event-date svg { position: absolute; inset: 0; }
  .event-date__text {
    position: relative;
    margin: 0;
    height: 56px;
    text-align: center;
    line-height: 56px;
    padding-top: 4px;
    box-sizing: border-box;
    font-size: 32px;
    font-weight: 400;
    color: var(--ribbon-text);
    white-space: nowrap;
  }
</style>
</head>
<body>
<main class="poster">
  <svg class="book-frame" viewBox="0 0 1200 777" xmlns="http://www.w3.org/2000/svg">
    <!-- top edge -->
    <g role="img" aria-label="Orange book lying at an angle">
      <polygon points="-10,-10 110,-10 145,112 18,152" fill="var(--book-orange)"/>
    </g>
    <g role="img" aria-label="Open book with blank pages">
      <polygon points="210,-10 445,-10 400,150 188,90" fill="var(--book-page)"/>
    </g>
    <g role="img" aria-label="Brown book spine">
      <rect x="532" y="-10" width="48" height="112" rx="12" fill="var(--book-brown)"/>
    </g>
    <g role="img" aria-label="Orange book spine">
      <rect x="582" y="-10" width="52" height="142" rx="12" fill="var(--book-orange)"/>
    </g>
    <g role="img" aria-label="Red book spine">
      <rect x="636" y="-10" width="48" height="128" rx="12" fill="var(--book-red)"/>
    </g>
    <g role="img" aria-label="Teal book lying at an angle">
      <polygon points="786,-10 928,-10 910,124 768,96" fill="var(--book-teal)"/>
    </g>
    <g role="img" aria-label="Orange book lying at an angle">
      <polygon points="990,-10 1136,-10 1094,112 972,66" fill="var(--book-orange)"/>
    </g>

    <!-- left stack -->
    <g role="img" aria-label="Stack of books seen from the spine side">
      <rect x="-20" y="182" width="158" height="44" rx="12" fill="var(--book-brown)"/>
      <rect x="-20" y="227" width="204" height="44" rx="12" fill="var(--book-teal)"/>
      <rect x="-20" y="272" width="191" height="44" rx="12" fill="var(--book-red)"/>
      <rect x="-20" y="317" width="172" height="44" rx="12" fill="var(--book-orange)"/>
      <rect x="-20" y="362" width="184" height="44" rx="12" fill="var(--book-teal)"/>
      <rect x="-20" y="407" width="158" height="44" rx="12" fill="var(--book-brown)"/>
      <rect x="-20" y="452" width="192" height="44" rx="12" fill="var(--book-red)"/>
      <rect x="-20" y="497" width="157" height="44" rx="12" fill="var(--book-orange)"/>
    </g>

    <!-- right stack -->
    <g role="img" aria-label="Stack of books seen from the page edges">
      <rect x="1080" y="128" width="140" height="40" rx="12" fill="var(--book-red)"/>
      <rect x="1056" y="170" width="164" height="40" rx="12" fill="var(--book-brown)"/>
      <rect x="1086" y="212" width="134" height="40" rx="12" fill="var(--book-orange)"/>
      <rect x="1052" y="254" width="168" height="40" rx="12" fill="var(--book-teal)"/>
      <rect x="1056" y="296" width="164" height="40" rx="12" fill="var(--book-red)"/>
      <rect x="1042" y="338" width="178" height="42" rx="12" fill="var(--book-orange)"/>
      <rect x="1070" y="382" width="150" height="40" rx="12" fill="var(--book-brown)"/>
    </g>
    <g role="img" aria-label="Teal book standing at an angle">
      <polygon points="1126,444 1220,470 1220,640 1076,596" fill="var(--book-teal)"/>
    </g>

    <!-- bottom edge -->
    <g role="img" aria-label="Open book with a teal cover">
      <polygon points="-10,610 150,580 204,740 140,790 -10,790" fill="var(--book-page)"/>
    </g>
    <g role="img" aria-label="Brown book lying at an angle">
      <polygon points="272,680 412,660 424,790 268,790" fill="var(--book-brown)"/>
    </g>
    <g role="img" aria-label="Red book lying at an angle">
      <polygon points="540,652 684,668 670,790 524,790" fill="var(--book-red)"/>
    </g>
    <g role="img" aria-label="Orange book lying at an angle">
      <polygon points="748,684 892,652 912,790 760,790" fill="var(--book-orange)"/>
    </g>
    <g role="img" aria-label="Three books leaning against each other">
      <rect x="1000" y="712" width="40" height="110" rx="4" fill="var(--book-teal)" transform="rotate(-28 1020 767)"/>
      <rect x="1040" y="650" width="46" height="170" rx="4" fill="var(--book-orange)" transform="rotate(-28 1063 735)"/>
      <rect x="1090" y="638" width="52" height="180" rx="4" fill="var(--book-red)" transform="rotate(-28 1116 728)"/>
    </g>
  </svg>

  <p class="guild-mark">CSG</p>

  <div class="union-mark">
    <span class="union-mark__dot"></span>
    <span class="union-mark__name">KWNU</span>
  </div>

  <h1 class="event-title">PYDB</h1>

  <p class="event-tagline">
    <svg viewBox="0 0 24 24" aria-hidden="true"><polygon points="12,1 15,9 23,9 16.5,14 19,22 12,17 5,22 7.5,14 1,9 9,9"/></svg>
    <span class="event-tagline__text">Pause Your Day And Browse</span>
    <svg viewBox="0 0 24 24" aria-hidden="true"><polygon points="12,1 15,9 23,9 16.5,14 19,22 12,17 5,22 7.5,14 1,9 9,9"/></svg>
  </p>

  <div class="event-date">
    <svg viewBox="0 0 392 56" width="392" height="56" aria-hidden="true">
      <polygon points="0,0 392,0 380,28 392,56 0,56 12,28" fill="var(--ribbon)"/>
    </svg>
    <p class="event-date__text">OCTOBER 23, 2017</p>
  </div>
</main>
</body>
</html>
```